Flyer Design

we need a flyer design for a new company Amberleaf Garden maintenance
we want a leaflet for our gardening services.
we do lawn cutting,hedge cutting, lawn treatments,tree work, full garden maintenance.
I have attached some ones i like so this might give you a starting point.

Industry/Entity Type

It Company

```html
<!DOCTYPE html>
<html lang="en">
<head>
<meta charset="utf-8">
<title>Amberleaf Garden maintenance – Flyer</title>
<link href="https://fonts.googleapis.com/css2?family=Roboto+Condensed:wght@700&display=swap" rel="stylesheet">
<style>
  :root {
    --navy: #1f2a6b;
    --royal: #2739a3;
    --lavender: #a9a7dc;
    --lavender-soft: #dcdbf0;
    --ink: #1d1d1f;
    --white: #ffffff;
    --leaf-dark: #2f5a22;
    --leaf-mid: #5f8f3a;
    --leaf-light: #9cc36a;
    --porch-blue: #4a6290;
  }
  html, body {
    margin: 0;
    padding: 0;
    width: 1200px;
    height: 850px;
    overflow: hidden;
    background: var(--white);
  }
  .flyer {
    position: relative;
    width: 1200px;
    height: 850px;
    overflow: hidden;
    font-family: "Roboto Condensed", "Arial Narrow", sans-serif;
    font-weight: 700;
  }
  .garden-photo {
    position: absolute;
    inset: 0;
    background:
      linear-gradient(180deg, rgba(74,98,144,0.85) 0%, rgba(74,98,144,0.55) 35%, rgba(0,0,0,0) 55%),
      linear-gradient(90deg, var(--porch-blue) 0%, var(--leaf-mid) 30%, var(--leaf-dark) 60%, var(--leaf-light) 100%);
  }
  .shapes {
    position: absolute;
    inset: 0;
  }
  .brand {
    position: absolute;
    left: 830px;
    top: 150px;
    display: flex;
    align-items: center;
    gap: 16px;
    color: var(--navy);
  }
  .brand-mark {
    width: 62px;
    height: 62px;
    background: var(--navy);
  }
  .brand-name {
    margin: 0;
    font-size: 44px;
    line-height: 0.95;
    text-transform: uppercase;
    letter-spacing: 0.5px;
  }
  .brand-name span {
    display: block;
    font-size: 19px;
    letter-spacing: 1.4px;
    margin-top: 6px;
  }
  .services-heading {
    position: absolute;
    left: 850px;
    top: 351px;
    width: 350px;
    height: 71px;
    margin: 0;
    box-sizing: border-box;
    padding-right: 45px;
    background: var(--lavender-soft);
    color: var(--royal);
    font-size: 42px;
    line-height: 71px;
    text-align: right;
  }
  .services-list {
    position: absolute;
    right: 45px;
    top: 452px;
    margin: 0;
    padding: 0;
    list-style: none;
    text-align: right;
    color: var(--ink);
    font-size: 35px;
    line-height: 51px;
  }
  .call-band {
    position: absolute;
    left: 0;
    top: 762px;
    width: 780px;
    height: 70px;
    background: var(--royal);
    display: flex;
    align-items: center;
    gap: 22px;
    padding-left: 68px;
    box-sizing: border-box;
    color: var(--white);
    font-size: 42px;
    letter-spacing: 1px;
  }
  .call-icon {
    width: 46px;
    height: 46px;
  }
</style>
</head>
<body>
<div class="flyer">
  <div class="garden-photo" role="img" aria-label="Photo of a blue house porch with a hanging flower basket, clipped shrubs and a red flower bed on a green lawn"></div>

  <svg class="shapes" width="1200" height="850" viewBox="0 0 1200 850" aria-hidden="true">
    <path class="panel" d="M800 0 C720 300 730 600 830 850 L1200 850 L1200 0 Z" fill="#ffffff" fill-opacity="0.88"/>
    <path class="swoosh" d="M715 0 C655 260 675 600 785 850 L830 850 C730 600 722 300 800 0 Z" fill="#2739a3"/>
    <path class="swoosh-accent" d="M812 0 C765 110 762 210 790 320 C792 210 830 100 895 0 Z" fill="#a9a7dc"/>
  </svg>

  <div class="brand">
    <div class="brand-mark"></div>
    <h1 class="brand-name">Amberleaf<span>Garden maintenance</span></h1>
  </div>

  <h2 class="services-heading">OUR SERVICES</h2>
  <ul class="services-list">
    <li>GRASS CUTTING</li>
    <li>HEDGE CUTTING</li>
    <li>TIDY UPS</li>
    <li>WEEDING</li>
    <li>TREE WORK</li>
    <li>FULL GARDEN</li>
    <li>MAINTENANCE</li>
  </ul>

  <div class="call-band">
    <span class="call-label">CALL NOW</span>
    <svg class="call-icon" viewBox="0 0 46 46" aria-hidden="true">
      <circle cx="23" cy="23" r="20" fill="none" stroke="#ffffff" stroke-width="3"/>
      <path d="M16 13 l5 0 l2 6 l-3 2 c1.5 3 3.5 5 6 6 l2 -3 l6 2 l0 5 c-10 1 -19 -8 -18 -18 z" fill="#ffffff"/>
    </svg>
    <span class="call-number">07700 900481</span>
  </div>
</div>
</body>
</html>
```